Executive Performance Review mapped on J-curve

I need to turn an executive company performance review into a visual infographic. The list of accomplishments is grouped into four calendar quarters. Each quarter needs a subtle representation of the season. The four quarters and associated list of accomplishments need to be mapped to a J-curve. - Spreadsheet with accomplishments attached (Throughput)- Sample image of a J-curve. You can google J-curve to see more images.- The title should be "Danela Morsky Year in Review"

Target Market(s)

Board of Directors

Requirements
Nice to have
• This will be presented to a company founder that is an artist and customer experience expert. He is very visual so a nice visual representation of the data will be impactful. He also uses the phrase that you have to live with or work with someone for four seasons before you really know them. This is why I have the seasons mapped to the quarters. The Fall season motif should be gloomy and stormy.

```html
<!DOCTYPE html>
<html lang="en">
<head>
<meta charset="utf-8">
<title>Danela Morsky Year in Review</title>
<link href="https://fonts.googleapis.com/css2?family=Roboto+Condensed:wght@400;700&family=Roboto:wght@300;400;500;700&display=swap" rel="stylesheet">
<style>
  :root{
    --summer:#F9B90F; --summer-dark:#E9AE08;
    --fall:#F44336; --fall-dark:#E0261E;
    --winter:#03A9F4; --winter-dark:#0288D1;
    --spring:#8E44AD; --spring-dark:#7A2CA3;
    --value:#8BC34A; --value-dark:#7CB342;
    --ink:#8C8C8C; --icon:#7A7A7A; --rule:#B9B9B9;
  }
  *{box-sizing:border-box;margin:0;padding:0}
  html,body{width:1200px;height:960px;overflow:hidden;background:#fff}
  .canvas{position:relative;width:1200px;height:960px;overflow:hidden;background:#fff;font-family:"Roboto",sans-serif}

  .divider{position:absolute;top:48px;height:850px;border-left:1.5px dashed var(--rule)}

  .season-head{position:absolute;top:0;width:240px;height:40px;color:#fff;
    font-family:"Roboto Condensed",sans-serif;font-weight:700;font-size:28px;text-align:center;line-height:41px;letter-spacing:.5px}
  .quarter-pill{position:absolute;top:40px;width:84px;height:27px;border-radius:0 0 9px 9px;color:#fff;
    font-weight:300;font-size:17px;text-align:center;line-height:27px}
  .pill-shadow{position:absolute;top:79px;width:84px;height:4px;border-radius:50%;background:radial-gradient(#e3e3e3,transparent 70%)}

  .summer{--c:var(--summer)} .fall{--c:var(--fall)} .winter{--c:var(--winter)} .spring{--c:var(--spring)}

  .block{position:absolute;width:228px;z-index:3}
  .block .icon{width:24px;height:24px;display:block;color:var(--icon)}
  .block h3{font-family:"Roboto Condensed",sans-serif;font-weight:700;font-size:13.4px;color:var(--c);line-height:14px;margin-top:3px;letter-spacing:.2px}
  .block ul{list-style:none;margin-top:1px}
  .block li{position:relative;padding-left:9.5px;font-size:9.6px;line-height:11.45px;color:var(--ink);font-weight:300}
  .block li::before{content:"";position:absolute;left:1px;top:4.3px;width:4px;height:4px;border-radius:50%;background:var(--c)}

  .curve{position:absolute;left:0;top:0;z-index:1}
  .badge{position:absolute;z-index:4}
  .badge-label{position:absolute;width:100%;text-align:center;color:#fff;font-family:"Roboto Condensed",sans-serif;font-weight:700;font-size:14.5px}

  .phase-band{position:absolute;left:0;top:890px;width:960px;height:45px;z-index:2;
    background:linear-gradient(90deg,#F19A22 0%,#EE7A2A 22%,#D95846 40%,#8E6F8A 55%,#4E8FDB 72%,#6F5CC6 88%,#8246B8 100%)}
  .phase{position:absolute;top:0;width:240px;text-align:center;color:#fff;font-weight:500;font-size:20.5px;line-height:45px}
  .effect-band{position:absolute;left:0;top:935px;width:960px;height:25px;overflow:hidden;z-index:2;
    background:linear-gradient(90deg,#F79B1C,#EC5B39 35%,#6A82C8 60%,#3D8DE2 75%,#8A4BBE)}
  .effect-letter{position:absolute;top:-2px;width:30px;margin-left:-15px;text-align:center;font-family:"Roboto Condensed",sans-serif;font-weight:700;font-size:34px;line-height:40px}

  .value-panel{position:absolute;left:960px;top:0;width:240px;height:960px;background:var(--value)}
  .value-head{position:absolute;left:0;top:0;width:240px;height:40px;background:var(--value-dark);color:#fff;
    font-family:"Roboto Condensed",sans-serif;font-weight:700;font-size:28px;text-align:center;line-height:41px}
  .value-pill{left:78px;background:#74AD3C}
  .greenfield{position:absolute;left:1080px;top:588px;transform:translate(-50%,-50%) rotate(-90deg);color:#fff;
    font-weight:700;font-size:100px;letter-spacing:-2px;white-space:nowrap;line-height:1;z-index:3}
</style>
</head>
<body>
<div class="canvas">

  <svg width="0" height="0" style="position:absolute">
    <defs>
      <symbol id="i-transition" viewBox="0 0 24 24"><g fill="none" stroke="currentColor" stroke-width="1.3"><path d="M11 4H3v17h17v-8"/><path d="M14 3h7v7M21 3 11 13"/></g></symbol>
      <symbol id="i-arch" viewBox="0 0 24 24"><g fill="none" stroke="currentColor" stroke-width="1.2"><circle cx="5" cy="12" r="3.2"/><path d="m3.6 12 1 1 2-2"/><path d="M8.2 12h4M12.2 5v14M12.2 5h3M12.2 12h3M12.2 19h3"/><rect x="15.2" y="2.5" width="4.5" height="5"/><rect x="15.2" y="9.5" width="4.5" height="5"/><rect x="15.2" y="16.5" width="4.5" height="5"/></g></symbol>
      <symbol id="i-strategy" viewBox="0 0 24 24"><g fill="none" stroke="currentColor" stroke-width="1.3"><path d="m2 7 4 4M6 7l-4 4"/><path d="M8 17c5 0 6-5 6-12"/><path d="m11 7 3-3 3 3"/><circle cx="18" cy="19" r="2.5"/></g></symbol>
      <symbol id="i-sales" viewBox="0 0 24 24"><g fill="none" stroke="currentColor" stroke-width="1.3"><path d="M13 4h6v6L10 19l-6-6z"/><circle cx="16" cy="7" r="1.2"/><path d="M19 5c2-2 3-1 3 0"/><path d="m8 12 3 3M10 11l2 2"/></g></symbol>
      <symbol id="i-revenue" viewBox="0 0 24 24"><g fill="none" stroke="currentColor" stroke-width="1.3"><path d="M9 3h6l-2 4h-2z"/><path d="M11 7C5 10 4 21 12 21s7-11 1-14"/><path d="M14 11c-1-1-4-1-4 1s4 1 4 3-3 2-4 1M12 9.5v9"/></g></symbol>
      <symbol id="i-hire" viewBox="0 0 24 24"><g fill="none" stroke="currentColor" stroke-width="1.3"><circle cx="10" cy="10" r="7.5"/><circle cx="10" cy="10" r="5.5"/><circle cx="10" cy="8.5" r="1.8"/><path d="M6.8 13.5c1-2 5.4-2 6.4 0"/><path d="m15.5 15.5 5 5"/><rect x="17" y="17" width="3" height="5" transform="rotate(-45 18.5 19.5)"/></g></symbol>
    </defs>
  </svg>

  <!-- Season headers -->
  <div class="season-head" style="left:0;background:var(--summer)">SUMMER</div>
  <div class="season-head" style="left:240px;background:var(--fall)">FALL</div>
  <div class="season-head" style="left:480px;background:var(--winter)">WINTER</div>
  <div class="season-head" style="left:720px;background:var(--spring)">SPRING</div>

  <div class="quarter-pill" style="left:75px;background:var(--summer-dark)">Q3 2018</div>
  <div class="quarter-pill" style="left:318px;background:var(--fall-dark)">Q4 2018</div>
  <div class="quarter-pill" style="left:558px;background:var(--winter-dark)">Q1 2019</div>
  <div class="quarter-pill" style="left:798px;background:var(--spring-dark)">Q2 2019</div>
  <div class="pill-shadow" style="left:78px"></div>
  <div class="pill-shadow" style="left:318px"></div>
  <div class="pill-shadow" style="left:558px"></div>
  <div class="pill-shadow" style="left:798px"></div>

  <div class="divider" style="left:240px"></div>
  <div class="divider" style="left:480px"></div>
  <div class="divider" style="left:720px"></div>

  <!-- J-curve -->
  <svg class="curve" width="960" height="960" viewBox="0 0 960 960" role="img" aria-label="J-curve rising through four seasonal scenes: summer fruit and butterflies, stormy autumn leaves and rain, winter snowflakes and pines, spring blossoms and flowers">
    <defs>
      <linearGradient id="fill-seasons" x1="0" x2="1" y1="0" y2="0">
        <stop offset="0" stop-color="#FBB51A"/>
        <stop offset=".22" stop-color="#F6862A"/>
        <stop offset=".34" stop-color="#E9573C"/>
        <stop offset=".5" stop-color="#8C8296"/>
        <stop offset=".56" stop-color="#4FA6E4"/>
        <stop offset=".72" stop-color="#2E8CE6"/>
        <stop offset=".86" stop-color="#5B66CF"/>
        <stop offset="1" stop-color="#8C45B8"/>
      </linearGradient>
      <linearGradient id="edge-seasons" x1="0" x2="1" y1="0" y2="0">
        <stop offset="0" stop-color="#FDC42B"/>
        <stop offset=".25" stop-color="#FDC42B"/>
        <stop offset=".27" stop-color="#F44336"/>
        <stop offset=".5" stop-color="#F44336"/>
        <stop offset=".5" stop-color="#03A9F4"/>
        <stop offset=".74" stop-color="#03A9F4"/>
        <stop offset=".76" stop-color="#8E44AD"/>
        <stop offset="1" stop-color="#8E44AD"/>
      </linearGradient>
      <linearGradient id="ground" x1="0" x2="0" y1="0" y2="1">
        <stop offset="0" stop-color="#fff" stop-opacity="0"/>
        <stop offset="1" stop-color="#fff" stop-opacity=".18"/>
      </linearGradient>
    </defs>
    <path d="M0,506 C70,610 150,700 260,727 C360,750 440,735 520,700 C640,650 700,600 800,500 C870,432 920,400 960,367 L960,890 L0,890 Z" fill="url(#fill-seasons)"/>
    <path d="M0,820 Q240,860 480,845 T960,860 L960,890 L0,890 Z" fill="url(#ground)"/>
    <path d="M0,506 C70,610 150,700 260,727 C360,750 440,735 520,700 C640,650 700,600 800,500 C870,432 920,400 960,367" fill="none" stroke="url(#edge-seasons)" stroke-width="5"/>
  </svg>

  <!-- Summer -->
  <section class="block summer" style="left:15px;top:84px">
    <svg class="icon"><use href="#i-transition"/></svg>
    <h3>TRANSITIONS</h3>
    <ul><li>RO Transition from Theo &amp; Mira</li><li>Start CR Office Initiative</li><li>Tactical Ops transition from Theo</li><li>Formalize Exec Team</li></ul>
  </section>
  <section class="block summer" style="left:15px;top:172px">
    <svg class="icon"><use href="#i-arch"/></svg>
    <h3>BIZ ARCHITECTURE</h3>
    <ul><li>Independent Financial Audit</li><li>Organizational Audit - Structure</li><li>Organizational Audit - People</li><li>XF Framework - ESU</li><li>Defined Utilization, Realization, Availability</li></ul>
  </section>
  <section class="block summer" style="left:15px;top:280px">
    <svg class="icon"><use href="#i-strategy"/></svg>
    <h3>STRATEGY</h3>
    <ul><li>Effective Strategy Meeting</li><li>Strategic Themes 2018 - 2020: Stablize, Accelerate, Surge</li><li>Business Drivers: Drive Revenue, Improve Norvite Experience, Increase Brand Awareness</li></ul>
  </section>
  <section class="block summer" style="left:15px;top:391px">
    <svg class="icon"><use href="#i-sales"/></svg>
    <h3>SALES</h3>
    <ul><li>Halvers Account Transition</li><li>QRN Account Transition</li><li>2 year Managed Services Engagement Model</li></ul>
  </section>
  <section class="block summer" style="left:15px;top:470px">
    <svg class="icon"><use href="#i-revenue"/></svg>
    <h3>REVENUE / EBITA</h3>
    <ul><li>TBD</li></ul>
  </section>

  <!-- Fall -->
  <section class="block fall" style="left:253px;top:80px">
    <svg class="icon"><use href="#i-arch"/></svg>
    <h3>BIZ ARCHITECTURE</h3>
    <ul><li>XF Framework - Functional Meetings &amp; Scrum of Scrums</li><li>Structured Reorg</li><li>Implemented Reorg</li><li>Quarterly Org Iteration cadence</li><li>Defined Key Hire Plan</li><li>CR Office Operational</li><li>Time Accountability</li><li>Tools ReConfig</li><li>Org Structure v1</li></ul>
  </section>
  <section class="block fall" style="left:253px;top:251px">
    <svg class="icon"><use href="#i-strategy"/></svg>
    <h3>STRATEGY</h3>
    <ul><li>Internal QBR Accountability</li></ul>
  </section>
  <section class="block fall" style="left:253px;top:314px">
    <svg class="icon"><use href="#i-sales"/></svg>
    <h3>SALES</h3>
    <ul><li>Kestrel QBR</li><li>Halvers QBR</li></ul>
  </section>
  <section class="block fall" style="left:253px;top:394px">
    <svg class="icon"><use href="#i-revenue"/></svg>
    <h3>REVENUE / EBITA</h3>
    <ul><li>TBD</li></ul>
  </section>

  <!-- Winter -->
  <section class="block winter" style="left:494px;top:80px">
    <svg class="icon"><use href="#i-arch"/></svg>
    <h3>BIZ ARCHITECTURE</h3>
    <ul><li>XF Framework - Progress Demos</li><li>Org Structure - COE's</li><li>Stablize Accounting &amp; Finance</li><li>Exec Hiring Process</li></ul>
  </section>
  <section class="block winter" style="left:494px;top:182px">
    <svg class="icon"><use href="#i-hire"/></svg>
    <h3>KEY HIRES</h3>
    <ul><li>Controller</li><li>Director CX</li></ul>
  </section>
  <section class="block winter" style="left:494px;top:258px">
    <svg class="icon"><use href="#i-strategy"/></svg>
    <h3>STRATEGY</h3>
    <ul><li>Founders removed from front line activity</li><li>Norvo QBR - Goal Setting &amp; Tracking</li></ul>
  </section>
  <section class="block winter" style="left:494px;top:333px">
    <svg class="icon"><use href="#i-sales"/></svg>
    <h3>SALES</h3>
    <ul><li>QRN QBR</li><li>Halvers QBR</li></ul>
  </section>
  <section class="block winter" style="left:494px;top:410px">
    <svg class="icon"><use href="#i-revenue"/></svg>
    <h3>REVENUE / EBITA</h3>
    <ul><li>TBD</li></ul>
  </section>

  <!-- Spring -->
  <section class="block spring" style="left:734px;top:80px">
    <svg class="icon"><use href="#i-arch"/></svg>
    <h3>BIZ ARCHITECTURE</h3>
    <ul><li>Tiered Pricing Pre-Paid Engagement Model</li><li>XF Framework - Ideation Board</li><li>Consulting Levels &amp; Salary Bands</li><li>Roles &amp; Responsibilities</li></ul>
  </section>
  <section class="block spring" style="left:734px;top:182px">
    <svg class="icon"><use href="#i-hire"/></svg>
    <h3>KEY HIRES</h3>
    <ul><li>Interim HR</li><li>Provisional Client Partner</li><li>Acting Director 1</li><li>Acting Director 2</li><li>Client Partner 1</li><li>Sales Exec 1</li></ul>
  </section>
  <section class="block spring" style="left:734px;top:302px">
    <svg class="icon"><use href="#i-sales"/></svg>
    <h3>SALES</h3>
    <ul><li>Opened BrightFrame Door</li><li>Flipped focus from operationaly run company to sales/marketing driven org</li><li>JLT Direct</li></ul>
  </section>
  <section class="block spring" style="left:734px;top:400px">
    <svg class="icon"><use href="#i-revenue"/></svg>
    <h3>REVENUE / EBITA</h3>
    <ul><li>TBD</li></ul>
  </section>

  <!-- Curve badges -->
  <div class="badge" style="left:59px;top:585px;width:110px;height:110px">
    <svg width="110" height="110" viewBox="0 0 110 110">
      <circle cx="55" cy="55" r="54" fill="#fff" opacity=".35"/>
      <circle cx="55" cy="55" r="50" fill="var(--summer)" stroke="#fff" stroke-width="4"/>
      <g fill="none" stroke="#fff" stroke-width="1.6">
        <path d="M38 47a8 8 0 0 1 9-9 10 10 0 0 1 18 3 7 7 0 0 1 1 13H40a6 6 0 0 1-2-7z"/>
        <circle cx="66" cy="34" r="5"/><path d="M66 24v3M74 34h3M72 28l2-2"/>
        <path d="m54 54-4 7h5l-3 6"/><path d="M40 60l-3 4M46 60l-3 4"/>
      </g>
    </svg>
    <div class="badge-label" style="top:72px">Storming</div>
  </div>

  <div class="badge" style="left:305px;top:697px;width:110px;height:110px">
    <svg width="110" height="110" viewBox="0 0 110 110">
      <circle cx="55" cy="55" r="54" fill="#fff" opacity=".35"/>
      <circle cx="55" cy="55" r="50" fill="var(--fall)" stroke="#fff" stroke-width="4"/>
      <path d="M32 44h9l4-10 6 30 5-22 4 10h13" fill="none" stroke="#fff" stroke-width="2" stroke-linejoin="round"/>
    </svg>
    <div class="badge-label" style="top:70px">Activity</div>
  </div>

  <div class="badge" style="left:545px;top:616px;width:110px;height:110px">
    <svg width="110" height="110" viewBox="0 0 110 110">
      <circle cx="55" cy="55" r="54" fill="#fff" opacity=".35"/>
      <circle cx="55" cy="55" r="50" fill="var(--winter)" stroke="#fff" stroke-width="4"/>
      <g fill="none" stroke="#fff" stroke-width="1.6">
        <circle cx="63" cy="30" r="8" stroke-dasharray="3 2"/><circle cx="63" cy="30" r="5"/>
        <circle cx="46" cy="51" r="8" stroke-dasharray="3 2"/><circle cx="46" cy="51" r="5"/>
        <path d="M34 36v-5h8M42 28l3 3-3 3M74 46v5h-8M66 48l-3 3 3 3"/>
      </g>
    </svg>
    <div class="badge-label" style="top:72px">Throughput</div>
  </div>

  <div class="badge" style="left:784px;top:440px;width:110px;height:110px">
    <svg width="110" height="110" viewBox="0 0 110 110">
      <circle cx="55" cy="55" r="54" fill="#fff"/>
      <circle cx="55" cy="55" r="50" fill="var(--spring)"/>
      <g fill="none" stroke="#fff" stroke-width="1.8">
        <path d="M31 22v34h35"/>
        <path d="M36 48l10-8 8 5 12-11"/>
        <circle cx="36" cy="48" r="2.5"/><circle cx="46" cy="40" r="2.5"/><circle cx="54" cy="45" r="2.5"/><circle cx="67" cy="33" r="2.5"/>
      </g>
    </svg>
    <div class="badge-label" style="top:70px">Outcomes</div>
  </div>

  <!-- Phase band -->
  <div class="phase-band">
    <div class="phase" style="left:0">Assessment</div>
    <div class="phase" style="left:240px">Stablize</div>
    <div class="phase" style="left:480px">Stractical</div>
    <div class="phase" style="left:720px">Strategic</div>
  </div>
  <div class="effect-band">
    <span class="effect-letter" style="left:70px;color:#FFE33B">E</span>
    <span class="effect-letter" style="left:136px;color:#FFD233">F</span>
    <span class="effect-letter" style="left:206px;color:#FFC23A">F</span>
    <span class="effect-letter" style="left:273px;color:#FF9D60">E</span>
    <span class="effect-letter" style="left:342px;color:#FF9AA0">C</span>
    <span class="effect-letter" style="left:412px;color:#FFB8C8">T</span>
    <span class="effect-letter" style="left:473px;color:#F5EEF5">I</span>
    <span class="effect-letter" style="left:537px;color:#5FE0FF">V</span>
    <span class="effect-letter" style="left:609px;color:#4FD7F4">E</span>
    <span class="effect-letter" style="left:676px;color:#4AD0F2">N</span>
    <span class="effect-letter" style="left:749px;color:#59D6F0">E</span>
    <span class="effect-letter" style="left:818px;color:#D8B8F6">S</span>
    <span class="effect-letter" style="left:888px;color:#E1C3FA">S</span>
  </div>

  <!-- Value creation -->
  <div class="value-panel">
    <div class="value-head">VALUE CREATION</div>
    <div class="quarter-pill value-pill">2020</div>
    <svg style="position:absolute;left:0;top:0" width="240" height="960" viewBox="0 0 240 960">
      <line x1="84" y1="278" x2="0" y2="367" stroke="#fff" stroke-width="3"/>
      <circle cx="120" cy="234" r="57" fill="#fff" stroke="var(--value-dark)" stroke-width="4"/>
      <circle cx="120" cy="234" r="53" fill="#fff"/>
      <g fill="none" stroke="var(--value)" stroke-width="1.8">
        <path d="M95 204v38h42"/>
        <path d="M102 232l10-9 8 5 12-12"/>
        <circle cx="102" cy="232" r="2.5"/><circle cx="112" cy="223" r="2.5"/><circle cx="120" cy="228" r="2.5"/><circle cx="133" cy="215" r="2.5"/>
      </g>
      <text x="120" y="262" text-anchor="middle" fill="var(--value-dark)" font-family="Roboto Condensed, sans-serif" font-weight="700" font-size="14.5">Outcomes</text>
    </svg>
  </div>
  <div class="greenfield">Greenfield</div>

</div>
</body>
</html>
```